Post Card Mailer for QUIK PATH PROSPECTS using new logo

We need a post card designed to send through the USA mail service that will go to new prospective clients.

The post card will introduce me and my new company and try to educate them our on company and services.

The goal is for them to call me or email me so I can have a discussion and try to sell our product.

Our product is a name list of individuals that are looking for consulting / help to determine if they qualify for USA social security benefits and then help to manage the process. We sell this name list to law firms that help these individuals.

Our services are better because we have a better less expensive way to identify people via the internet that want help. Our conversion rate is 15%, so every 100 leads a law firm buys the will obtain 15 customers / clients.

Designer on Logo took alot longer than expected. Also there were two projects that needed to combined into one. Which was done yesterday.

Target Market(s)

Law firms

Font styles to use
Serif
Sans Serif
Script

Colors

Designer to choose colors to be used in the design.

Requirements
Must have
• The size of the mailer should be about 6 by 8 inches.
• Two sides.
• Side 1: With our Logo and key messages we want to communicate.
• Side 2: A space to be used by the USA mail services in lower right, my photo and an introduction by me to our company and why they should buy from my company.
Nice to have
• Images that represent what we do, how we help, and our target market.
Should not have
• Poor taste in images that upset people

```html
<!DOCTYPE html>
<html lang="en">
<head>
<meta charset="utf-8">
<title>QUIK PATH PROSPECTS – Postcard Mailer</title>
<link href="https://fonts.googleapis.com/css2?family=Exo+2:ital,wght@0,500;0,600;0,700;1,600;1,700&family=Lato:ital,wght@0,300;0,400;0,700;0,900;1,400;1,700;1,900&display=swap" rel="stylesheet">
<style>
  :root {
    --page: #e9ebee;
    --navy: #1e2b3d;
    --navy-deep: #141d2a;
    --brand-blue: #1565b0;
    --bright-blue: #1f77c9;
    --sky: #4fc2ee;
    --cloud-light: #5fc3f0;
    --grey-word: #8d99a8;
    --charcoal: #3a3b3d;
    --dark-band: #2b2c2e;
    --ink: #2f3033;
    --muted: #6c6f74;
    --white: #ffffff;
    --rule: #b9bcc1;
  }
  * { box-sizing: border-box; margin: 0; padding: 0; }
  html, body { width: 902px; height: 1200px; overflow: hidden; }
  body {
    background: var(--page);
    font-family: "Lato", Arial, sans-serif;
    color: var(--ink);
    position: relative;
  }
  .card {
    position: absolute;
    width: 664px;
    height: 497px;
    background: var(--white);
    overflow: hidden;
    box-shadow: 0 2px 8px rgba(0,0,0,.18);
  }
  .card--front { left: 52px; top: 72px; }
  .card--back { left: 163px; top: 626px; }

  /* ---------- FRONT ---------- */
  .word-cloud {
    position: absolute; left: 0; top: 0; width: 339px; height: 430px;
    background: radial-gradient(ellipse at 30% 55%, #34465e 0%, var(--navy) 55%, var(--navy-deep) 100%);
    color: var(--white);
  }
  .cloud-row {
    position: absolute; left: 28px; right: 6px;
    display: flex; align-items: baseline; gap: 7px; white-space: nowrap;
  }
  .cloud-row--right { justify-content: flex-end; }
  .w-grey { color: var(--grey-word); font-weight: 300; }
  .w-blue { color: var(--cloud-light); font-weight: 700; }
  .w-bold { font-weight: 700; }
  .cloud-brand {
    position: absolute; left: 30px; top: 186px; width: 190px;
    font-family: "Exo 2", sans-serif; font-weight: 700; font-size: 27px;
    line-height: 1.05; color: #3f8fdc; letter-spacing: .5px;
  }
  .brand-mark {
    display: flex; align-items: center; gap: 10px;
    font-family: "Exo 2", sans-serif; font-weight: 700; color: var(--brand-blue);
    letter-spacing: .5px; line-height: 1.05;
  }
  .brand-mark .square { width: 14px; height: 14px; background: var(--muted); flex: none; }
  .front-brand { position: absolute; left: 412px; top: 26px; font-size: 24px; width: 230px; }

  .feature-photo { position: absolute; width: 123px; height: 99px; border: 1px solid #8a8d92; }
  .photo-a { left: 372px; top: 115px; background: linear-gradient(180deg,#f4f4f4 0%,#d8d8d8 60%,#3a3a3a 85%,#c8202a 100%); }
  .photo-b { left: 509px; top: 115px; background: radial-gradient(circle at 50% 40%,#4c8fd8 0%,#6b7f96 40%,#b8c1cc 100%); }
  .photo-c { left: 372px; top: 279px; background: linear-gradient(135deg,#6fa3d4 0%,#d9b8a4 50%,#4b86c4 100%); }
  .photo-d { left: 509px; top: 279px; background: linear-gradient(135deg,#a8322f 0%,#c9a15a 45%,#3a3e5a 100%); }
  .feature { position: absolute; width: 140px; }
  .feature h3 {
    font-family: "Exo 2", sans-serif; font-weight: 700; font-size: 8.5px;
    color: var(--bright-blue); letter-spacing: .3px; margin-bottom: 3px;
  }
  .feature li {
    list-style: none; font-size: 7px; font-style: italic; color: var(--ink);
    padding-left: 10px; position: relative; line-height: 1.3; margin-bottom: 4px;
  }
  .feature li::before {
    content: ""; position: absolute; left: 0; top: 2px;
    width: 5px; height: 5px; border-radius: 50%; background: var(--bright-blue);
  }
  .feat-1 { left: 374px; top: 227px; }
  .feat-2 { left: 511px; top: 227px; }
  .feat-3 { left: 374px; top: 389px; }
  .feat-4 { left: 511px; top: 389px; }

  .contact-band {
    position: absolute; left: 0; top: 430px; width: 664px; height: 67px;
    background: linear-gradient(90deg, #2540a0 0%, var(--bright-blue) 55%, var(--sky) 100%);
  }
  .contact-dark {
    position: absolute; left: 380px; top: 430px; width: 284px; height: 43px;
    background: var(--dark-band);
    clip-path: polygon(0 0, 100% 0, 100% 100%, 40px 100%);
  }
  .contact-name {
    position: absolute; left: 17px; top: 442px; color: var(--white);
    font-size: 15px; font-weight: 700; line-height: 1;
  }
  .contact-name small { display: block; font-size: 9px; font-weight: 400; margin-top: 3px; }
  .contact-phone {
    position: absolute; left: 136px; top: 440px; display: flex; align-items: center; gap: 8px;
    font-family: "Exo 2", sans-serif; font-weight: 700; font-size: 25px; color: var(--white);
  }
  .contact-email {
    position: absolute; left: 418px; top: 443px; display: flex; align-items: center; gap: 9px;
    color: var(--white); font-size: 15px; font-weight: 700;
  }

  /* ---------- BACK ---------- */
  .intro-hero { position: absolute; left: 0; top: 0; width: 365px; height: 158px; background: var(--brand-blue); }
  .portrait {
    position: absolute; left: 32px; top: 29px; width: 109px; height: 129px;
    border: 3px solid var(--white);
    background: linear-gradient(180deg,#e8e9ec 0%,#c9b8ad 45%,#2d3544 100%);
  }
  .name-plate {
    position: absolute; left: 141px; top: 66px; width: 224px; height: 36px;
    background: linear-gradient(90deg,#d9dadd 0%,#f3f3f4 60%,#ffffff 100%);
    padding: 5px 0 0 15px; font-size: 11px; font-weight: 700; color: var(--charcoal); line-height: 1.3;
  }
  .intro-heading {
    position: absolute; left: 0; top: 165px; width: 365px; height: 51px;
    background: var(--charcoal); color: var(--white);
    font-family: "Exo 2", sans-serif; font-weight: 600; font-size: 15px;
    letter-spacing: .6px; line-height: 1.25; padding: 8px 0 0 12px;
  }
  .intro-points { position: absolute; left: 22px; top: 235px; width: 340px; }
  .intro-points li {
    list-style: none; font-size: 10.5px; color: var(--ink); line-height: 1.3;
    padding-left: 27px; position: relative; margin-bottom: 4px;
  }
  .intro-points li svg { position: absolute; left: 0; top: 2px; }
  .intro-callout {
    position: absolute; left: 0; top: 381px; width: 365px; height: 87px;
    background: var(--brand-blue); color: var(--white);
    font-size: 17.5px; font-weight: 900; font-style: italic; line-height: 1.3; padding: 11px 0 0 36px;
  }
  .back-footer { position: absolute; left: 0; top: 473px; width: 664px; height: 24px; background: var(--charcoal); }

  .back-brand { position: absolute; left: 440px; top: 32px; font-size: 22px; width: 200px; }
  .tagline {
    position: absolute; left: 376px; top: 108px; width: 288px; text-align: center;
    font-size: 8.5px; font-style: italic; font-weight: 700; color: var(--ink); line-height: 1.35;
  }
  .test-heading {
    position: absolute; left: 380px; top: 150px;
    font-family: "Exo 2", sans-serif; font-weight: 700; font-size: 15px; color: var(--bright-blue); letter-spacing: .5px;
  }
  .test-points { position: absolute; left: 380px; top: 174px; }
  .test-points li {
    list-style: none; font-size: 12.5px; font-weight: 900; font-style: italic; color: var(--ink);
    padding-left: 24px; position: relative; margin-bottom: 5px;
  }
  .test-points li::before {
    content: ""; position: absolute; left: 0; top: 4px; width: 9px; height: 9px; border-radius: 50%; background: var(--bright-blue);
  }
  .mail-panel {
    position: absolute; left: 366px; top: 252px; width: 282px; height: 217px;
    border: 1px solid var(--rule); border-bottom: none;
  }
  .return-address {
    position: absolute; left: 13px; top: 14px; font-size: 7.5px; line-height: 1.35; color: var(--muted);
  }
  .stamp-box { position: absolute; left: 196px; top: 12px; width: 69px; height: 60px; border: 1px solid var(--rule); }
  .address-line { position: absolute; left: 66px; width: 199px; height: 1px; background: var(--charcoal); }
</style>
</head>
<body>

<!-- Front side -->
<section class="card card--front">
  <div class="word-cloud">
    <div class="cloud-row" style="top:40px"><span class="w-bold" style="font-size:11px">Tailored Campaigns</span><span class="w-bold" style="font-size:14px">Passion</span><span style="font-size:8px">100 years of cumulative experience</span></div>
    <div class="cloud-row" style="top:62px"><span class="w-grey" style="font-size:8px">Technology SaVVY</span><span style="font-size:15px;font-weight:300">Proprietary Software and Methods</span></div>
    <div class="cloud-row" style="top:86px"><span style="font-size:9px">LOW COST ACQUISITION</span><span class="w-blue" style="font-size:14px">Best Leads, Best Price</span><span style="font-size:11px">Exclusivity</span></div>
    <div class="cloud-row" style="top:111px"><span class="w-grey" style="font-size:14px">Best Conversion Rates</span><span style="font-size:15px;font-weight:300">SSD Domain Expertise</span></div>
    <div class="cloud-row" style="top:136px;left:82px"><span style="font-size:13px">Deep business and process acumen</span></div>
    <div class="cloud-row cloud-row--right" style="top:157px"><span class="w-grey" style="font-size:14px">Systems Integration</span></div>
    <div class="cloud-brand">QUIK PATH<br>PROSPECTS</div>
    <div class="cloud-row" style="top:188px;left:237px"><span style="font-size:12.5px">Quality Standards</span></div>
    <div class="cloud-row" style="top:216px;left:258px"><span style="font-size:12px">Referrals</span></div>
    <div class="cloud-row" style="top:244px;left:240px"><span style="font-size:17px">Highest ROI</span></div>
    <div class="cloud-row" style="top:275px;left:35px"><span class="w-blue" style="font-size:20px;font-weight:400">Reliable, Dependable, Helpful</span></div>
    <div class="cloud-row" style="top:304px"><span style="font-size:10px">Tested leads generation practices</span><span style="font-size:12px">Great data mining &amp; filters</span></div>
    <div class="cloud-row" style="top:323px;left:62px;gap:38px"><span style="font-size:14px">Trusted Partner</span><span style="font-size:14px">Exclusivity</span></div>
    <div class="cloud-row" style="top:344px;left:30px;gap:10px"><span class="w-grey" style="font-size:10px">Technology R&amp;D Investment</span><span class="w-grey" style="font-size:14px">Experienced at outsourcing</span></div>
    <div class="cloud-row" style="top:366px;left:69px;gap:32px"><span style="font-size:9px">Easy to use</span><span style="font-size:10px;color:#c9d0d8">Benchmarking &amp; Consulting</span></div>
    <div class="cloud-row" style="top:384px;left:25px;gap:8px"><span style="font-size:12.5px">High Volume Generation</span><span class="w-grey" style="font-size:13.5px">Age Demographics (35 to 64)</span></div>
  </div>

  <div class="brand-mark front-brand"><span class="square"></span><span>QUIK PATH<br>PROSPECTS</span></div>

  <div class="feature-photo photo-a" role="img" aria-label="Business people standing on columns, one on a red block"></div>
  <div class="feature-photo photo-b" role="img" aria-label="People facing a wall of screens around a glowing globe"></div>
  <div class="feature-photo photo-c" role="img" aria-label="Caring hands holding an elderly person's hand"></div>
  <div class="feature-photo photo-d" role="img" aria-label="Scales of justice and gavel in front of a flag"></div>

  <div class="feature feat-1"><h3>BEST LEADS, BEST PRICE</h3><ul><li>Our high conversation rates lowers your client acquisition cost</li><li>Referrals available</li></ul></div>
  <div class="feature feat-2"><h3>HIGH VOLUME, QUALITY LEADS</h3><ul><li>50 years of SSD domain knowledge</li><li>Tested technology capabilities</li></ul></div>
  <div class="feature feat-3"><h3>TRUSTED PARTNER</h3><ul><li>Reliability, Dependable, Helpful</li><li>Deep business &amp; process acumen</li></ul></div>
  <div class="feature feat-4"><h3>QUIK TO USE</h3><ul><li>Integrate seamlessly into your IT systems</li><li>Tailored campaigns</li></ul></div>

  <div class="contact-band"></div>
  <div class="contact-dark"></div>
  <div class="contact-name">Marcus Dellane,<small>President QUIK PATH PROSPECTS</small></div>
  <div class="contact-phone">
    <svg width="22" height="22" viewBox="0 0 22 22" aria-hidden="true"><circle cx="11" cy="11" r="9.5" fill="none" stroke="#fff" stroke-width="1.6"/><path d="M8 6.5c.6-.4 1.2-.2 1.5.4l.8 1.6c.2.5 0 1-.4 1.3l-.6.4c.5 1.2 1.3 2.1 2.5 2.7l.5-.6c.3-.4.9-.5 1.3-.3l1.6.9c.5.3.7 1 .3 1.5-.8 1-2.1 1.4-3.3.8-2.3-1.1-4.1-3-5-5.4-.4-1.2 0-2.6.8-3.3z" fill="#fff"/></svg>
    <span>555-318-2047</span>
  </div>
  <div class="contact-email">
    <svg width="16" height="12" viewBox="0 0 16 12" aria-hidden="true"><rect x="0" y="0" width="16" height="12" fill="#fff"/><path d="M0 0l8 6.5L16 0" fill="none" stroke="#2b2c2e" stroke-width="1.3"/></svg>
    <span>marcus@quikpathprospects.com</span>
  </div>
</section>

<!-- Back side -->
<section class="card card--back">
  <div class="intro-hero"></div>
  <div class="portrait" role="img" aria-label="Portrait photo of the company president"></div>
  <div class="name-plate">Marcus Dellane<br>President, QUIK PATH PROSPECTS</div>
  <h2 class="intro-heading">I WANT TO PERSONALLY INTRODUCE<br>OUR COMPANY TO YOU!</h2>
  <ul class="intro-points">
    <li><svg width="10" height="10" viewBox="0 0 10 10" aria-hidden="true"><circle cx="5" cy="5" r="4.3" fill="none" stroke="#1f77c9" stroke-width=".9"/><path d="M4 3l2 2-2 2" fill="none" stroke="#1f77c9" stroke-width=".9"/></svg>My team as &gt; 50 years of cumulative SSD experience.</li>
    <li><svg width="10" height="10" viewBox="0 0 10 10" aria-hidden="true"><circle cx="5" cy="5" r="4.3" fill="none" stroke="#1f77c9" stroke-width=".9"/><path d="M4 3l2 2-2 2" fill="none" stroke="#1f77c9" stroke-width=".9"/></svg>We have proven technology that delivers the best leads.</li>
    <li><svg width="10" height="10" viewBox="0 0 10 10" aria-hidden="true"><circle cx="5" cy="5" r="4.3" fill="none" stroke="#1f77c9" stroke-width=".9"/><path d="M4 3l2 2-2 2" fill="none" stroke="#1f77c9" stroke-width=".9"/></svg>The timing is right for a new competitor in this industry.</li>
    <li><svg width="10" height="10" viewBox="0 0 10 10" aria-hidden="true"><circle cx="5" cy="5" r="4.3" fill="none" stroke="#1f77c9" stroke-width=".9"/><path d="M4 3l2 2-2 2" fill="none" stroke="#1f77c9" stroke-width=".9"/></svg>I had to come out of retirement after 30 years with Norvell Industries, the opportunity is just that great … I love building businesses and partnering with great customers!</li>
    <li><svg width="10" height="10" viewBox="0 0 10 10" aria-hidden="true"><circle cx="5" cy="5" r="4.3" fill="none" stroke="#1f77c9" stroke-width=".9"/><path d="M4 3l2 2-2 2" fill="none" stroke="#1f77c9" stroke-width=".9"/></svg>Our business, industry, &amp; technical acumen is unrivaled … and we can do it at a cost than no others can.</li>
  </ul>
  <p class="intro-callout">Let’s work together to bring Social<br>Security Disability benefits to those<br>in need and deserving!</p>

  <div class="brand-mark back-brand"><span class="square"></span><span>QUIK PATH<br>PROSPECTS</span></div>
  <p class="tagline">Best Leads … Best Price with High Volume &amp; Quality capacity …<br>Leads from a Trusted Partner that is QUIK to use</p>
  <h2 class="test-heading">TEST OUR LEADS</h2>
  <ul class="test-points">
    <li>Start at 250 or 500 Leads.</li>
    <li>Grow to 1,000 … 3,000 or even 10,000!</li>
    <li>We give the right support to your growth.</li>
  </ul>

  <div class="mail-panel">
    <address class="return-address" style="font-style:normal">
      Marcus Dellane, President QUIK PATH PROSPECTS<br>
      1210 Larkspur Avenue, Suite 400<br>
      Dayton Ohio 45402<br>
      555-318-2047<br>
      marcus@quikpathprospects.com
    </address>
    <div class="stamp-box"></div>
    <div class="address-line" style="top:117px"></div>
    <div class="address-line" style="top:148px"></div>
    <div class="address-line" style="top:179px"></div>
  </div>

  <div class="back-footer"></div>
</section>

</body>
</html>
```